TW Groundworks Capability Statement

I need to design a two page Capability statement for our Civil Construction company that looks professional and can be issued to clients in electronic or print form to show our capabilities.

We have an existing Logo and website https://twgroundworks.com.au/

It should include space for the below:
- Company heading/logo plus ABN, ACN and full contact details
- About Us – Mission, vision, values
- Our Service Offering / Core competencies
- Accreditations/certifications

Designs look the same

```html
<!DOCTYPE html>
<html lang="en">
<head>
<meta charset="utf-8">
<title>TW Groundworks – Capability Statement</title>
<link href="https://fonts.googleapis.com/css2?family=Fira+Sans:wght@300;400;600;700&display=swap" rel="stylesheet">
<style>
:root{
  --navy:#2d2a7b;
  --band:#4d4a93;
  --band-dark:#3b3883;
  --gold:#f5a81c;
  --ink:#2b2b2b;
  --paper:#ffffff;
  --bg:#ffffff;
}
*{margin:0;padding:0;box-sizing:border-box}
html,body{width:1200px;height:848px;overflow:hidden;background:var(--bg)}
body{font-family:"Fira Sans",sans-serif;color:var(--ink);position:relative}
.page{position:absolute;top:76px;width:502px;height:709px;background:var(--paper);box-shadow:0 2px 6px rgba(0,0,0,.18);overflow:hidden}
.page--front{left:66px}
.page--back{left:653px}
.footer{position:absolute;left:0;bottom:0;width:100%;height:40px;background:var(--navy);color:var(--gold);font-weight:700;font-size:16px;letter-spacing:.5px;text-align:center;line-height:40px}
/* front header */
.hero{position:absolute;left:0;top:0;width:502px;height:178px;background:linear-gradient(120deg,var(--band-dark),var(--band) 55%,#6a67a6);overflow:hidden}
.logo-panel{position:absolute;left:0;top:0}
.brand{position:absolute;display:flex;align-items:center;gap:7px;font-weight:700;color:var(--navy)}
.brand__mark{background:var(--gold)}
.hero .brand{left:66px;top:30px;font-size:22px}
.hero .brand__mark{width:26px;height:26px}
.contact{position:absolute;right:35px;top:11px;text-align:right;color:#fff;font-size:8px;line-height:12px}
.contact b{font-weight:600}
.hero__title{position:absolute;left:36px;top:126px;color:#fff;font-weight:700;font-size:28px;line-height:28px;letter-spacing:.5px}
h2.section{position:absolute;color:var(--navy);font-weight:700;font-size:17px;letter-spacing:.3px}
.body{position:absolute;font-size:9.6px;line-height:12.1px;font-weight:300;color:var(--ink)}
.col h3{color:var(--navy);font-weight:700;font-size:17px;margin-bottom:8px}
.col{position:absolute;top:314px;width:125px}
.col p{font-size:9.6px;line-height:12.1px;font-weight:300}
.divider{position:absolute;top:330px;width:1px;height:100px;background:#c9c9d8}
.comp{position:absolute;left:36px;display:flex;align-items:center;gap:11px;font-size:12.5px;font-weight:300}
.comp__icon{width:20px;height:20px;background:var(--gold)}
.trait__icon{position:absolute;top:577px;width:36px;height:36px;border-radius:50%;background:var(--navy)}
.trait{position:absolute;top:620px;width:64px;text-align:center;font-size:7.6px;line-height:10px;font-weight:300;color:#444}
.accred{position:absolute;left:252px;top:445px;width:215px;height:208px;border:2px solid var(--navy);border-radius:8px}
.accred__title{position:absolute;left:0;top:-8px;width:100%;text-align:center;color:var(--navy);font-weight:700;font-size:17px;line-height:21px;letter-spacing:.5px}
.accred__title span{background:#fff;padding:0 6px}
.badge{position:absolute;top:52px;width:70px;height:70px;border-radius:50%;border:5px solid var(--navy)}
/* back page */
.back-head .brand{left:58px;top:22px;font-size:20px}
.back-head .brand__mark{width:22px;height:22px}
.call{position:absolute;right:36px;top:15px;text-align:right;font-size:8px;line-height:12px;color:var(--navy)}
.call b{font-weight:700}
.band{position:absolute;left:0;top:67px;width:502px;height:180px;background:linear-gradient(100deg,var(--band-dark),var(--band) 60%,#5d5a9e)}
.band__title{position:absolute;right:323px;top:100px;text-align:right;color:#fff;font-weight:700;font-size:20px;line-height:29px;letter-spacing:1px}
.band__rule{position:absolute;left:218px;top:108px;width:2px;height:120px;background:#fff}
.band__text{position:absolute;left:252px;top:94px;width:204px;text-align:right;color:#fff;font-weight:600;font-size:7.7px;line-height:10.1px}
.tab{position:absolute;height:32px;background:var(--navy);color:#fff;font-weight:700;font-size:17px;line-height:32px}
.photo{position:absolute;border-radius:8px}
</style>
</head>
<body>

<section class="page page--front">
  <header class="hero">
    <svg class="logo-panel" width="260" height="90" viewBox="0 0 260 90"><polygon points="39,0 228,0 252,86 64,86" fill="#fff"/></svg>
    <div class="brand"><span class="brand__mark"></span>TW Groundworks</div>
    <div class="contact">
      <b>Find Us</b><br>5/18 Carrington Road,<br>Derrimut VIC 3026<br>
      <b>Call Us</b><br>Daniel Hargrave 0400 123 456<br>Marcus Tiller 0412 555 018<br>
      <b>E mail Us</b><br>tenders@twgroundworks.com.au<br><br>
      <b>ABN 12 345 678 901</b><br><b>ACN 000 000 123</b>
    </div>
    <h1 class="hero__title">CAPABILITIES<br>STATEMENT</h1>
  </header>

  <h2 class="section" style="left:36px;top:196px">ABOUT TW GROUNDWORKS</h2>
  <p class="body" style="left:36px;top:218px;width:432px">TW Groundworks is a specialist utilities contractor leveraging industry experience to provide exceptional outcomes. We are a client focused business that takes a ‘best-for-project’ approach in everything we do, and see honest, timely and transparent communication as one of our key strengths. Our business works in complex, high-risk environments and understands all safety, quality, and environmental considerations. We meticulously plan our projects with these key factors in mind, ensuring the requirements of the specific tasks are understood and well documented to satisfy our robust internal processes and rigorous external auditing.</p>

  <div class="col" style="left:37px"><h3>Our Mission</h3><p>Lorem ipsum dolor sit amet, consectetuer adipiscing elit, sed diam nonummy nibh euismod tincidunt ut laoreet dolore magna aliquam erat volutpat. Ut wisi enim ad</p></div>
  <div class="divider" style="left:169px"></div>
  <div class="col" style="left:184px"><h3>Our Vision</h3><p>Lorem ipsum dolor sit amet, consectetuer adipiscing elit, sed diam nonummy nibh euismod tincidunt ut laoreet dolore magna aliquam erat volutpat. Ut wisi enim ad</p></div>
  <div class="divider" style="left:320px"></div>
  <div class="col" style="left:335px"><h3>Our Values</h3><p>Lorem ipsum dolor sit amet, consectetuer adipiscing elit, sed diam nonummy nibh euismod tincidunt ut laoreet dolore magna aliquam erat volutpat. Ut wisi enim ad</p></div>

  <h2 class="section" style="left:37px;top:438px">CORE COMPETENCIES</h2>
  <div class="comp" style="top:470px"><span class="comp__icon"></span>Project / Program Management</div>
  <div class="comp" style="top:495px"><span class="comp__icon"></span>Water Infrastructure</div>
  <div class="comp" style="top:519px"><span class="comp__icon"></span>Gas Infrastructure</div>
  <div class="comp" style="top:544px"><span class="comp__icon"></span>Civil Construction</div>

  <span class="trait__icon" style="left:47px"></span>
  <span class="trait__icon" style="left:97px"></span>
  <span class="trait__icon" style="left:143px"></span>
  <span class="trait__icon" style="left:190px"></span>
  <div class="trait" style="left:33px">Trusted<br>Professionals</div>
  <div class="trait" style="left:83px">Safety<br>Focused</div>
  <div class="trait" style="left:129px">Quality<br>Assurance</div>
  <div class="trait" style="left:176px">Collaborative<br>Problem<br>Solvers</div>

  <div class="accred">
    <div class="accred__title"><span>ACCREDITATIONS</span><br>&amp;CERTIFICATIONS</div>
    <span class="badge" style="left:18px"></span>
    <span class="badge" style="left:118px"></span>
  </div>

  <footer class="footer">www.twgroundworks.com.au</footer>
</section>

<section class="page page--back">
  <header class="back-head">
    <div class="brand"><span class="brand__mark"></span>TW Groundworks</div>
    <div class="call"><b>CALL US</b><br>Daniel Hargrave 0400 123 456<br>Marcus Tiller 0412 555 018</div>
  </header>

  <div class="band" role="img" aria-label="Tinted photo of a civil construction site"></div>
  <h2 class="band__title">OUR<br>SERVICE<br>OFFERING</h2>
  <span class="band__rule"></span>
  <p class="band__text">TW Groundworks prides itself on being a customer focused business, that takes the time to understand our clients’ key drivers and ensure we work collaboratively with them to achieve positive outcomes. We have a team of highly experienced project management professionals who are genuine, responsive, and transparent which enables us to make our client lives easier from the design phase to project completion. We have a self-perform field resource that carries enviable experience, which is supplemented by hand-picked sub-contractors that are known in the industry and are trusted partners.</p>

  <div class="tab" style="left:0;top:265px;width:233px;padding-left:36px">Utilities</div>
  <p class="body" style="left:34px;top:301px;width:202px">Our team has a wide-ranging utilities background which gives us a deep understanding of what is in the ground and the specific requirements for each individual asset. Through this experience we have developed relationships with asset owners and distributors to ensure we deliver projects that will stand the test of time and be valuable pieces of future networks. Our commitment to safety and quality has further strengthened these relationships and puts us in a position to be a trusted advisor when the inevitable challenges are faced.</p>

  <div class="photo" style="left:289px;top:266px;width:177px;height:177px;background:linear-gradient(160deg,#8a7560,#3f5fa8 45%,#a08c72)" role="img" aria-label="Photo of blue valves and copper pipework installed on site"></div>
  <div class="photo" style="left:34px;top:472px;width:177px;height:178px;background:linear-gradient(180deg,#e9e6e2,#9aa5a4 45%,#5a4a3c)" role="img" aria-label="Photo of an excavator digging a trench"></div>

  <div class="tab" style="left:264px;top:461px;width:238px;text-align:center">Civil Construction</div>
  <p class="body" style="left:264px;top:501px;width:206px">Leveraging off our considerable utilities background, we have seen our civil construction offering continue to grow. We have a resource base of skilled operators who take immense pride in their work and enable us to deliver cost effective, efficient services. We maintain a ‘Tier 1’ mindset and hold ourselves to the highest standards, while still being an agile delivery partner that can be relied upon to deliver your next civil project.</p>

  <footer class="footer">www.twgroundworks.com.au</footer>
</section>

</body>
</html>
```